letterhead design using our existing logo

We are a small boutique property management business based in Sydney's Northern Beaches.
We are after a sleek, simple modern letterhead (A4) incorporating our logo and its colours.
Also matching envelope (DL)
I have attached the logo with black text and white text for design options.

Target Market(s)

29-69yo Male and Female

Industry/Entity Type

Property Management

Requirements
Must have
• - Keyhaven Estates logo
• - Address, number and website:
• Suite 7, 18-19 Harlow Parade, Brookvale NSW 2100
• Tel: Tom Carrick 0417 293 608 Lorena Adcock 0409 516 742 www.keyhavenestatesgroup.com.au
Nice to have
• sleek design that looks modern and professional
Should not have
• too many colours or too busy

```html
<!DOCTYPE html>
<html lang="en">
<head>
<meta charset="utf-8">
<title>Keyhaven Estates – Stationery</title>
<link href="https://fonts.googleapis.com/css2?family=Roboto+Condensed:wght@400;500;700&display=swap" rel="stylesheet">
<style>
  :root {
    --board: #a4a4a4;
    --paper: #ffffff;
    --ink: #111111;
    --teal: #0f7f86;
    --teal-dark: #0a6b78;
    --text-grey: #333333;
    --shadow: rgba(0,0,0,0.35);
  }
  * { margin: 0; padding: 0; box-sizing: border-box; }
  html, body { width: 1200px; height: 906px; overflow: hidden; }
  body {
    background: var(--board);
    font-family: "Roboto Condensed", "Arial Narrow", sans-serif;
    position: relative;
  }
  .sheet {
    position: absolute;
    background: var(--paper);
    box-shadow: 4px 5px 8px var(--shadow);
    overflow: hidden;
  }
  .letterhead { left: 50px; top: 100px; width: 504px; height: 714px; }
  .envelope-front { left: 596px; top: 142px; width: 565px; height: 283px; }
  .envelope-back { left: 596px; top: 465px; width: 565px; height: 282px; }

  .brand {
    display: flex;
    align-items: center;
    gap: 6px;
    color: var(--ink);
    font-weight: 500;
    text-transform: uppercase;
    letter-spacing: 0.2px;
    white-space: nowrap;
    line-height: 1;
  }
  .brand-mark { width: 7px; height: 7px; background: var(--teal); flex: none; }
  .letterhead .brand { position: absolute; left: 56px; top: 47px; font-size: 19px; }
  .envelope-back .brand {
    position: absolute; left: 50%; top: 38px;
    transform: translateX(-50%); font-size: 15px;
  }

  .letter-footer {
    position: absolute;
    left: 0; right: 0; top: 672px;
    text-align: center;
    color: var(--text-grey);
  }
  .contact-line { font-size: 7px; line-height: 9px; word-spacing: 0.5px; }
  .contact-line span { margin: 0 5px; }
  .contact-line b { color: var(--teal); font-weight: 700; }
  .letter-address {
    margin-top: 4px;
    font-size: 8px;
    line-height: 10px;
    font-weight: 500;
    color: var(--teal-dark);
  }

  .return-block {
    position: absolute; left: 26px; top: 231px;
    display: flex; align-items: center; gap: 12px;
  }
  .return-block .brand { font-size: 15px; }
  .return-divider { width: 1px; height: 19px; background: var(--teal); flex: none; }
  .return-address {
    font-size: 8.5px; line-height: 11px; color: var(--text-grey); white-space: nowrap;
  }
  .flap { position: absolute; left: 0; top: 0; }
</style>
</head>
<body>
  <section class="sheet letterhead">
    <div class="brand"><span class="brand-mark"></span>Keyhaven Estates</div>
    <footer class="letter-footer">
      <p class="contact-line">
        <span><b>P:</b> 0417 293 608 (Tom Carrick)</span>
        <span><b>P:</b> 0409 516 742 (Lorena Adcock)</span>
        <span><b>W:</b> www.keyhavenestatesgroup.com.au</span>
      </p>
      <p class="letter-address">Suite 7, 18-19 Harlow Parade, Brookvale NSW 2100</p>
    </footer>
  </section>

  <section class="sheet envelope-front">
    <div class="return-block">
      <div class="brand"><span class="brand-mark"></span>Keyhaven Estates</div>
      <div class="return-divider"></div>
      <p class="return-address">Suite 7, 18-19 Harlow Parade<br>Brookvale NSW 2100</p>
    </div>
  </section>

  <section class="sheet envelope-back">
    <svg class="flap" width="565" height="282" viewBox="0 0 565 282">
      <path d="M2 3 C 4 40, 8 75, 14 89 L 550 89 C 556 75, 561 40, 563 3"
            fill="none" stroke="#3a9aa3" stroke-width="1"/>
    </svg>
    <div class="brand"><span class="brand-mark"></span>Keyhaven Estates</div>
  </section>
</body>
</html>
```